SkyvoraQ Business Cards and Stationary Design

Need a design for our business cards and stationary. I want to carry on the theme of the logo. I want the business cards to have a design on the back. I would like the business cards and the stationary to carry the same theme, design scheme, and branding

Target Market(s)

Airlines and Maintenance Facilities

Industry/Entity Type

Aviation

Contact Information for Business Card

Name
Position Title
Address: 4827 Tollbeck Lane, Brindlewood, Calvera, 50318
Office Number
Mobile Number
Email
Website

Font styles to use
Serif
Sans Serif

Colors

Designer to choose colors to be used in the design.

```html
<!DOCTYPE html>
<html lang="en">
<head>
<meta charset="utf-8">
<title>SkyvoraQ Stationery</title>
<link rel="stylesheet" href="https://fonts.googleapis.com/css2?family=Montserrat:wght@400;600;800&family=Homemade+Apple&display=swap">
<style>
  :root {
    --navy: #0f1a3d;
    --navy-deep: #0a1230;
    --blue: #1f4fb4;
    --ink: #2a2f3d;
    --muted: #6b7283;
    --paper: #ffffff;
    --backdrop: #f1f2f4;
    --faint: #eef0f3;
  }
  * { box-sizing: border-box; margin: 0; padding: 0; }
  html, body { width: 1200px; height: 869px; overflow: hidden; }
  body { background: var(--backdrop); font-family: "Montserrat", Arial, sans-serif; color: var(--ink); position: relative; }

  .brand { display: flex; align-items: center; gap: 8px; position: relative; }
  .brand-dot { border-radius: 50%; background: var(--blue); flex: none; }
  .brand-name { font-weight: 800; color: var(--navy); letter-spacing: 0.12em; text-transform: uppercase; }

  /* Letterhead */
  .letterhead { position: absolute; left: 70px; top: 38px; width: 560px; height: 792px; background: var(--paper);
    box-shadow: 0 6px 18px rgba(0,0,0,0.12); padding: 58px 52px 0 52px; overflow: hidden; }
  .letterhead .brand-dot { width: 26px; height: 26px; }
  .letterhead .brand-name { font-size: 19px; }
  .watermark-ring { position: absolute; right: -70px; top: 270px; width: 330px; height: 330px; border-radius: 50%;
    border: 34px solid var(--faint); }
  .letter { position: relative; margin-top: 40px; font-size: 9.5px; line-height: 1.5; max-width: 440px; }
  .letter p { margin-bottom: 12px; }
  .recipient { margin-bottom: 14px; }
  .signature { font-family: "Homemade Apple", cursive; font-size: 15px; color: var(--navy); margin: 10px 0 4px; }
  .letter-foot { position: absolute; left: 0; right: 0; bottom: 0; height: 150px; }
  .letter-contact { position: absolute; right: 52px; bottom: 58px; text-align: right; font-size: 9px; color: var(--navy); line-height: 1.6; }
  .letter-contact .sep { color: var(--blue); padding: 0 5px; }
  .rule-navy { position: absolute; left: 0; bottom: 24px; width: 72%; height: 4px; background: var(--navy); }
  .rule-blue { position: absolute; right: 0; bottom: 24px; width: 28%; height: 8px; background: var(--blue); }

  /* Cards */
  .card { position: absolute; width: 420px; height: 240px; box-shadow: 0 6px 18px rgba(0,0,0,0.14); overflow: hidden; }
  .card-front { left: 700px; top: 150px; background: var(--paper); padding: 70px 36px; }
  .card-front .brand-dot { width: 22px; height: 22px; }
  .card-front .brand-name { font-size: 17px; }
  .card-front .watermark-ring { right: -50px; top: -40px; width: 170px; height: 170px; border-width: 18px; }
  .holder { position: relative; margin-top: 20px; border-left: 2px solid var(--blue); padding-left: 10px; }
  .holder-name { font-weight: 600; font-size: 13px; color: var(--navy); letter-spacing: 0.04em; }
  .holder-title { font-size: 8px; color: var(--blue); letter-spacing: 0.1em; margin-bottom: 6px; }
  .holder-line { font-size: 8px; color: var(--muted); line-height: 1.45; }

  .card-back { left: 700px; top: 470px; display: flex; flex-direction: column; align-items: center; justify-content: center; gap: 14px; }
  .card-back-ground { position: absolute; inset: 0; background: radial-gradient(circle at 50% 45%, #16234f 0%, var(--navy-deep) 75%); }
  .card-back .brand-dot { position: relative; width: 46px; height: 46px; background: transparent; border: 3px solid #ffffff; }
  .card-back .brand-name { position: relative; font-size: 24px; color: var(--blue); }
</style>
</head>
<body>

  <section class="letterhead">
    <div class="watermark-ring" aria-hidden="true"></div>
    <header class="brand">
      <span class="brand-dot"></span>
      <span class="brand-name">SkyvoraQ</span>
    </header>

    <article class="letter">
      <p class="recipient">November 1, 2015<br>Mr. Colin Ashby<br>88 Fernmoor Road<br>Oakhollow, Westmere 40217</p>
      <p>Dear Mr. Ashby<br>The first paragraph of a typical business letter is used to state the main point of the letter. Begin with a friendly opening, then quickly transition into the purpose of your letter. Use a couple of sentences to explain the purpose, but do not go in to detail until the next paragraph.</p>
      <p>Beginning with the second paragraph, state the supporting details to justify your purpose. These may take the form of background information, statistics or first-hand accounts. A few short paragraphs within the body of the letter should be enough to support your reasoning. Finally, in the closing paragraph, briefly restate your purpose and why it is important. If the purpose of your letter is related to your employment, consider ending your letter with your contact information and title if it is not included on letterhead.</p>
      <p>Finally, in the closing paragraph, briefly restate your purpose and why it is important. If the purpose of your letter is related to your employment, consider ending your letter with your contact information and title if it is not included on letterhead.</p>
      <p>Finally, in the closing paragraph, briefly restate your purpose and why it is important. If the purpose of your letter is related to your employment, consider ending your letter with your contact information and title if it is not included on letterhead. However, if the purpose is informational think about closing with gratitude for the reader's time.</p>
      <p>Sincerely,</p>
      <div class="signature">Ray Maddox</div>
      <p>President</p>
    </article>

    <footer class="letter-foot">
      <div class="letter-contact">
        0218846130<span class="sep">|</span>hello@skyvoraq.com<span class="sep">|</span>www.skyvoraq.com<br>
        4827 Tollbeck Lane, Brindlewood, Calvera, 50318
      </div>
      <div class="rule-navy"></div>
      <div class="rule-blue"></div>
    </footer>
  </section>

  <section class="card card-front">
    <div class="watermark-ring" aria-hidden="true"></div>
    <header class="brand">
      <span class="brand-dot"></span>
      <span class="brand-name">SkyvoraQ</span>
    </header>
    <div class="holder">
      <div class="holder-name">DALE RENWICK</div>
      <div class="holder-title">DIRECTOR</div>
      <div class="holder-line">0218846130</div>
      <div class="holder-line">hello@skyvoraq.com</div>
      <div class="holder-line">www.skyvoraq.com</div>
      <div class="holder-line">4827 Tollbeck Lane, Brindlewood, Calvera, 50318</div>
    </div>
  </section>

  <section class="card card-back">
    <div class="card-back-ground" role="img" aria-label="Deep navy background with a faint repeating brand pattern"></div>
    <span class="brand-dot"></span>
    <span class="brand-name">SkyvoraQ</span>
  </section>

</body>
</html>
```